Product Packaging Design for Luxury Make Up Brush Set-Minimal, Elegant, Chic

I need the packaging designed for new company, VÉLA, based in the United Kingdom. I have not developed the entire brand campaign yet, but I have a logo as attached. We are trying to emulate the 'feel' of RIV, Lumette, or Kirelo (https://www.kirelo-shop.example/) type of luxe style.
This is for a new brand of luxury and chic makeup brushes (and cosmetics organisers) called VÉLA. These are intelligently designed professional make up brushes that are designed to reflect a timeless elegance that incorporates chic trends in colours and materials. The cosmetic organizers and makeup brushes are European Chic; always stylish and intelligently designed. VÉLA in when form meets function in luxury cosmetics. What I am looking for now is packaging is for a 12-piece luxe makeup brush set. I have attached pictures of the set and a 'mood board' document with some images and fonts as well as the packaging diecut. Looking forward to discussing the details with the right designer. Thanks, Tova x
Updates

I have found a stock photo that has a very editorial feel and incorporates the neutral tones I like. I would like to see her on the front of the box. I have attached the image. Hope that fits into what you were planning. Thanks,Tova Added Friday, December 12, 2014

Target Market(s)

women, teenagers, make up artists and aficionados, those buying a gift for target market.

Industry/Entity Type

It Company

Font styles to use
Serif
Sans Serif
Script

Colors
000000
ffffff
757575
ceeae6
fff5ee
fee3d4
1b1b1b
e24096

Requirements
Must have
• I have attached another document titled 'make up brush descriptions' that has the details for the sales copy that needs to be on the packaging. Pictures of the set or at least a few brushes.
Nice to have
• I am not dead set on the colours I chose but I think less is more, classic black-white-neutral tones with perhaps a colour pop (like the dark pink/red I added). The brushes have rose-gold ferrules which should be shown in a pic(s) somewhere.
Should not have
• It should not look like the Belmi Professional box, I just uploaded it for some of the sales copy but have removed the photo as I wanted something original according to my brief. Also uploading a marketing image that is a great use of colours. That stock photo can be used in addition to the other if you see fit as well.
• Thanks, Tova

```html
<!DOCTYPE html>
<html lang="en">
<head>
<meta charset="utf-8">
<title>VÉLA Professional Brush Set</title>
<link rel="stylesheet" href="https://fonts.googleapis.com/css2?family=Bodoni+Moda:wght@500&family=Cormorant+Garamond:wght@500;600&family=Great+Vibes&display=swap">
<style>
  :root {
    --ink: #000000;
    --paper: #ffffff;
    --pop: #e24096;
    --pop-deep: #c0197f;
    --grey: #757575;
    --powder-violet: #5a2a9a;
    --powder-blue: #2c3fae;
  }
  * { margin: 0; padding: 0; box-sizing: border-box; }
  html, body {
    width: 1200px;
    height: 3820px;
    overflow: hidden;
    background: var(--ink);
  }
  .panel {
    position: relative;
    width: 1200px;
    height: 3820px;
    background: var(--ink);
    color: var(--paper);
    font-family: "Cormorant Garamond", Georgia, serif;
  }
  .hero-photo {
    position: absolute;
    left: 0; top: 0;
    width: 1200px; height: 1540px;
    background:
      radial-gradient(ellipse 320px 220px at 300px 460px, rgba(235,220,205,0.55), transparent 70%),
      radial-gradient(ellipse 280px 200px at 360px 560px, rgba(226,64,150,0.55), transparent 70%),
      radial-gradient(ellipse 320px 240px at 720px 360px, rgba(44,63,174,0.6), transparent 70%),
      radial-gradient(ellipse 260px 520px at 820px 980px, rgba(90,42,154,0.35), transparent 75%),
      var(--ink);
  }
  .brand-name {
    position: absolute;
    top: 1335px;
    width: 100%;
    text-align: center;
    font-family: "Bodoni Moda", "Didot", serif;
    font-weight: 500;
    font-size: 170px;
    letter-spacing: 4px;
    line-height: 1;
  }
  .product-line {
    position: absolute;
    top: 1620px;
    width: 100%;
    text-align: center;
    color: var(--pop);
    font-size: 74px;
    font-weight: 500;
    line-height: 1;
  }
  .product-name {
    position: absolute;
    top: 1720px;
    width: 100%;
    text-align: center;
    font-family: "Great Vibes", cursive;
    font-size: 140px;
    line-height: 1;
  }
  .section-title {
    display: flex;
    align-items: baseline;
    color: var(--pop);
    font-size: 56px;
    font-weight: 600;
    line-height: 1;
  }
  .section-title::after {
    content: "";
    flex: 1;
    margin-left: 6px;
    border-bottom: 3px dotted var(--pop);
  }
  .materials {
    position: absolute;
    left: 102px;
    top: 2068px;
    width: 912px;
  }
  .materials ul {
    list-style: none;
    margin-top: 20px;
  }
  .materials li {
    position: relative;
    padding-left: 80px;
    font-size: 60px;
    font-weight: 500;
    line-height: 83px;
  }
  .materials li::before {
    content: "";
    position: absolute;
    left: 16px;
    top: 36px;
    width: 14px; height: 14px;
    border-radius: 50%;
    background: var(--paper);
  }
  .animal-friendly {
    position: absolute;
    left: 360px;
    top: 2565px;
    width: 745px;
  }
  .animal-friendly p {
    margin-top: 14px;
    font-size: 60px;
    font-weight: 500;
    line-height: 82px;
  }
  .showcase {
    position: absolute;
    left: 0; top: 0;
    width: 1200px; height: 3820px;
    pointer-events: none;
  }
</style>
</head>
<body>
<main class="panel">
  <div class="hero-photo" role="img" aria-label="Two makeup brushes meeting against black with a burst of pink and violet powder"></div>

  <h1 class="brand-name">VÉLA</h1>
  <p class="product-line">Professional</p>
  <p class="product-name">Brush Set</p>

  <section class="materials">
    <h2 class="section-title">Material for each brush</h2>
    <ul>
      <li>Aluminium ferrule</li>
      <li>Baking varnish wooden handle</li>
      <li>Synthetic hair.</li>
      <li>PU leather cosmetic cylinder.</li>
    </ul>
  </section>

  <section class="animal-friendly">
    <h2 class="section-title">Animal Friendly</h2>
    <p>All our brushes are made from<br>soft synthetic hair.</p>
  </section>

  <svg class="showcase" viewBox="0 0 1200 3820" aria-hidden="false">
    <defs>
      <linearGradient id="brush-set-tone" x1="0" y1="0" x2="1" y2="0">
        <stop offset="0" stop-color="#ececec"/>
        <stop offset="0.5" stop-color="#d6d2d0"/>
        <stop offset="1" stop-color="#ececec"/>
      </linearGradient>
    </defs>
    <polygon class="accent-band" points="102,2731 1105,3104 1105,3152 102,2779" fill="#e24096"/>
    <polygon class="product-stage" points="102,2779 1105,3152 1105,3724 102,3724" fill="#ffffff"/>
    <rect role="img" aria-label="Twelve black-handled makeup brushes with rose-gold ferrules laid side by side"
          x="143" y="3010" width="910" height="630" rx="8" fill="url(#brush-set-tone)" opacity="0.7"/>
  </svg>
</main>
</body>
</html>
```